Varnel Co.,Ltd. need business card

Varnel Company Limited is a facility management company. We provides a total solution services from administration, energy saving, security, safety, food catering to companies.

The logo should be in elegant style with innovative that suited to the upper market
Please see the logo image in the attached file. You can use this Red or Blue or Green checkerboard (color and font should be similar to logo) as the main part of business card (can be an entire of one side of business card) . In another side of card should contain contact details of personnel - here below demo information

Kanyarat Wongdee
Chief Executive Officer

No.19, Soi 3, Rat Kaeo Road
Bang Muang, Bangkok,
10290, Thailand

Tel + 66915283064
Mobile + 66915283064
E-mail: Kanyarat.Wongdee@varnel-example.co.th

Target Market(s)

Factory, Hotel and Hospital

Industry/Entity Type

Business

Contact Information for Business Card

Kanyarat Wongdee
Chief Executive Officer

Bang Muang, Bangkok,
10290, Thailand

Tel + 66915283064
Mobile + 66915283064

We will change details with the winner designer

Font styles to use
Sans Serif

Requirements
Must have
• In style of red checkerboard and white color

```html
<!DOCTYPE html>
<html lang="en">
<head>
<meta charset="utf-8">
<title>Varnel Co.,Ltd. — Business Card</title>
<link rel="stylesheet" href="https://fonts.googleapis.com/css2?family=Source+Sans+3:ital,wght@0,400;0,600;1,400&display=swap">
<style>
  :root {
    --canvas: #ffffff;
    --card: #ffffff;
    --brand-red: #960404;
    --brand-red-dark: #7f0303;
    --accent-red: #d9141c;
    --ink: #161616;
    --reverse: #ffffff;
  }
  html, body {
    margin: 0;
    padding: 0;
    width: 1200px;
    height: 1000px;
    overflow: hidden;
    background: var(--canvas);
    font-family: "Source Sans 3", sans-serif;
    color: var(--ink);
  }
  .stage { position: relative; width: 1200px; height: 1000px; }
  .card {
    position: absolute;
    width: 555px;
    height: 380px;
    background: var(--card);
    box-shadow: 4px 5px 8px rgba(0,0,0,0.45);
    overflow: hidden;
  }
  .card--front { left: 172px; top: 97px; }
  .card--back { left: 479px; top: 497px; }

  .band {
    position: absolute;
    left: 0;
    width: 100%;
    background: linear-gradient(90deg, var(--brand-red), var(--brand-red-dark) 50%, var(--brand-red));
  }
  .card--front .band--top { top: 0; height: 55px; }
  .card--front .band--bottom { bottom: 0; height: 53px; }
  .card--back .band--main { top: 55px; height: 272px; }

  .person {
    position: absolute;
    left: 72px;
    top: 180px;
  }
  .person__name {
    margin: 0;
    font-size: 18px;
    font-weight: 600;
    line-height: 22px;
  }
  .person__role {
    margin: 0;
    font-size: 14px;
    font-style: italic;
    line-height: 18px;
  }
  .divider {
    position: absolute;
    left: 256px;
    top: 150px;
    width: 1.5px;
    height: 102px;
    background: var(--accent-red);
  }
  .contact {
    position: absolute;
    left: 282px;
    top: 152px;
    margin: 0;
    padding: 0;
    list-style: none;
    font-size: 10.5px;
    line-height: 13.3px;
  }
  .contact__item {
    position: relative;
    padding-left: 21px;
    margin-bottom: 7px;
  }
  .contact__icon {
    position: absolute;
    left: 0;
    width: 12px;
    height: 12px;
    fill: var(--accent-red);
  }
  .contact__item--address .contact__icon { top: 9px; }
  .contact__item--phone .contact__icon { top: 6px; }
  .contact__item--email .contact__icon { top: 1px; }

  .wordmark {
    position: absolute;
    left: 0;
    top: 55px;
    width: 100%;
    height: 272px;
    display: flex;
    align-items: center;
    justify-content: center;
    margin: 0;
    padding-left: 0.2em;
    box-sizing: border-box;
    font-size: 64px;
    font-weight: 400;
    letter-spacing: 0.2em;
    color: var(--reverse);
  }
</style>
</head>
<body>
<main class="stage">
  <section class="card card--front" aria-label="Business card front">
    <div class="band band--top" role="img" aria-label="Red checkerboard pattern band"></div>

    <div class="person">
      <h1 class="person__name">Kanyarat Wongdee</h1>
      <p class="person__role">Chief Executive Officer</p>
    </div>

    <div class="divider"></div>

    <ul class="contact">
      <li class="contact__item contact__item--address">
        <svg class="contact__icon" viewBox="0 0 12 12" aria-hidden="true"><path d="M6 0.5a4.2 4.2 0 0 0-4.2 4.2C1.8 7.8 6 11.5 6 11.5s4.2-3.7 4.2-6.8A4.2 4.2 0 0 0 6 0.5zm0 6a1.8 1.8 0 1 1 0-3.6 1.8 1.8 0 0 1 0 3.6z" fill-rule="evenodd"/></svg>
        No.19, Soi 3, Rat Kaeo Road<br>Bang Muang, Bangkok,<br>10290, Thailand
      </li>
      <li class="contact__item contact__item--phone">
        <svg class="contact__icon" viewBox="0 0 12 12" aria-hidden="true"><path d="M2.6 0.8l1.9 0.2 0.8 2.4-1.2 1a7 7 0 0 0 3.5 3.5l1-1.2 2.4 0.8 0.2 1.9c0 .7-.6 1.3-1.3 1.3C5.1 10.7 1.3 6.9 1.3 2.1c0-.7.6-1.3 1.3-1.3z"/></svg>
        Tel + 66915283064<br>Mobile + 66915283064
      </li>
      <li class="contact__item contact__item--email">
        <svg class="contact__icon" viewBox="0 0 12 12" aria-hidden="true"><path d="M0.5 2.5h11v7h-11z M0.5 2.5L6 6.6l5.5-4.1" stroke="#fff" stroke-width="0.8"/></svg>
        E-mail: Kanyarat.Wongdee@varnel-example.co.th
      </li>
    </ul>

    <div class="band band--bottom" role="img" aria-label="Red checkerboard pattern band"></div>
  </section>

  <section class="card card--back" aria-label="Business card back">
    <div class="band band--main" role="img" aria-label="Red checkerboard pattern panel"></div>
    <p class="wordmark">VARNEL</p>
  </section>
</main>
</body>
</html>
```